Identity Package (Logo, Website)

We need a logo and website design for a new company.
The new company is a voicemail transcription service provider. It's name is KL9BQZ.io
It will be very transactional. We like the "bootstrap" look and feel, and will be using a developer familiar with bootstrap. Here are the kinds of webpages we like :
https://www.lumenvane.io
http://www.quorbil.com/
http://www.plenivo.com/
There will only be 5 pages, as follows :
1- Homepage
2- Voicemail Transcription for Individuals
3- Voicemail Transcription for Companies
4- Wholesale Voicemail Transcription for Service Providers/Enterprises
5- Contact us
As far as the logo is concerned, we'd like to have just stylized text. It should be done in such a way as to make it easy to see the different elements of the name, which are KL, 2, and BQZ.
Reason: I have received a number of designs, but the designs are mostly from the same few designers (not that much variety in designers). I'd like a few more to compare if possible, so I thought I would keep this open until Monday to give more designers the opportunity to submit over the weekend. Thanks!

```html
<!DOCTYPE html>
<html lang="en">
<head>
<meta charset="utf-8">
<title>KL9BQZ.io – Voicemail Transcription</title>
<link rel="stylesheet" href="https://fonts.googleapis.com/css2?family=Open+Sans:wght@400;600;700&family=Oswald:wght@300&display=swap">
<style>
:root{
  --navy:#2c5470;
  --navy-text:#2b5a78;
  --sand:#f3dfae;
  --sand-deep:#e3c98a;
  --mint:#7ac1a8;
  --mint-dark:#5aa98d;
  --orange:#f09a2c;
  --footer:#46647a;
  --ink:#3a3a3a;
  --muted:#5b5b5b;
  --white:#ffffff;
  --cream:#f7e7b8;
}
*{box-sizing:border-box;margin:0;padding:0}
html,body{width:1200px;height:2748px;overflow:hidden}
body{font-family:"Open Sans",Arial,sans-serif;background:var(--white);position:relative;color:var(--ink)}
.brand{display:flex;align-items:center;gap:12px;color:var(--white);font-size:44px;font-weight:600;letter-spacing:-1px}
.brand-dot{width:40px;height:40px;border-radius:50%;background:var(--white)}

.site-header{position:absolute;top:0;left:0;width:1200px;height:92px;background:var(--navy)}
.site-header .brand{position:absolute;left:33px;top:18px}
.main-nav{position:absolute;top:0;left:0}
.main-nav a{position:absolute;top:38px;color:var(--white);text-decoration:none;font-size:17px;white-space:nowrap}
.login-btn{position:absolute;left:1070px;top:33px;width:90px;height:36px;border-radius:8px;background:var(--cream);color:var(--navy);font-size:17px;text-align:center;line-height:36px}

.hero{position:absolute;top:92px;left:0;width:1200px;height:549px;background:var(--sand)}
.hero h1{position:absolute;top:66px;width:100%;text-align:center;font-size:46px;font-weight:700;color:var(--navy-text)}
.hero-art{position:absolute;left:147px;top:164px;width:916px;height:385px;border-radius:12px 12px 0 0;background:linear-gradient(180deg,var(--sand-deep),#d9c08a)}

.intro{position:absolute;top:641px;left:0;width:1200px;height:425px;text-align:center}
.intro h2{margin-top:105px;font-size:46px;font-weight:700;color:var(--navy-text)}
.intro p{width:860px;margin:26px auto 0;font-size:29px;line-height:36px;color:var(--muted)}

.services{position:absolute;top:1066px;left:0;width:1200px;height:559px;background:var(--mint)}
.service{position:absolute;top:82px;width:330px;text-align:center;color:var(--white)}
.service-card{position:relative;width:260px;height:156px;margin:0 auto;background:var(--white);border-radius:8px}
.service-card::after{content:"";position:absolute;left:118px;bottom:-14px;border:12px solid transparent;border-top:14px solid var(--white);border-bottom:0}
.service-icon{position:absolute;left:90px;top:38px;width:80px;height:80px;border-radius:50%;background:var(--mint-dark)}
.service h3{margin-top:42px;font-size:25px;line-height:30px;font-weight:700}
.service p{margin:24px 0 0;padding:0 28px;text-align:left;font-size:17px;line-height:21px}

.testimonials{position:absolute;top:1625px;left:0;width:1200px;height:626px}
.testimonials h2{position:absolute;top:84px;width:100%;text-align:center;font-size:44px;font-weight:600;color:#333}
.quote{position:absolute;top:232px;width:330px}
.avatar{width:124px;height:124px;border-radius:50%;background:linear-gradient(180deg,#efe3d4,#d8c3aa);margin-bottom:36px}
.quote p{font-size:17px;line-height:21px;color:#333}
.quote .name{margin-top:10px;font-size:20px;font-weight:700;color:var(--mint-dark)}
.quote .role{font-size:14px;color:#777}

.cta{position:absolute;top:2251px;left:0;width:1200px;height:220px;background:var(--orange);text-align:center;color:var(--white)}
.cta p{margin-top:36px;font-size:37px}
.cta-btn{position:absolute;left:458px;top:105px;width:284px;height:81px;background:var(--white);display:flex;align-items:center;justify-content:center;gap:18px;color:var(--orange);font-size:27px;font-weight:700}

.site-footer{position:absolute;top:2471px;left:0;width:1200px;height:277px;background:var(--footer);color:var(--white)}
.site-footer .brand{position:absolute;left:33px;top:60px}
.copyright{position:absolute;left:33px;top:128px;font-size:14px}
.footer-col{position:absolute;top:68px}
.footer-col h4{font-size:24px;font-weight:700;margin-bottom:22px}
.social{display:flex;gap:16px}
.social span{width:54px;height:54px;border-radius:50%;background:#c9d5de}
.links{display:grid;grid-template-columns:114px 130px;font-size:17px;line-height:20px}
.contact{font-size:17px;line-height:21px}
.phone{display:flex;align-items:center;gap:10px;margin-top:6px;font-family:"Oswald",Arial,sans-serif;font-weight:300;font-size:38px}
</style>
</head>
<body>

<header class="site-header">
  <div class="brand"><span class="brand-dot"></span>kl9bqz</div>
  <nav class="main-nav">
    <a style="left:623px">FEATURES</a>
    <a style="left:749px">PRICING</a>
    <a style="left:857px">LEARNING</a>
    <a style="left:982px">SIGN UP</a>
  </nav>
  <div class="login-btn">LOGIN</div>
</header>

<section class="hero">
  <h1>Lorem ipsum dolor sit amet consectetuer</h1>
  <div class="hero-art" role="img" aria-label="Illustration of a hand holding a phone over a world map, surrounded by message bubbles, contact icons, an envelope and a voicemail badge"></div>
</section>

<section class="intro">
  <h2>Lorem ipsum dolor sit amet consectetuer</h2>
  <p>Ut wisi enim ad minim veniam, quis nostrud exerci tation ullamcorper suscipit lobortis nisl ut aliquip ex ea commodo consequat.</p>
</section>

<section class="services">
  <div class="service" style="left:29px">
    <div class="service-card"><div class="service-icon" role="img" aria-label="Icon of a single person"></div></div>
    <h3>Voicemail Transcription<br>for Individuals</h3>
    <p>Typi non habent claritatem insitam est usus legentis in iis qui facit eorum claritatem. Investigationes demonstraverunt lectores legere me lius quod ii legunt saepius.</p>
  </div>
  <div class="service" style="left:434px">
    <div class="service-card"><div class="service-icon" role="img" aria-label="Icon of a group of people"></div></div>
    <h3>Voicemail Transcription<br>for Companies</h3>
    <p>Typi non habent claritatem insitam est usus legentis in iis qui facit eorum claritatem. Investigationes demonsrunt lectores legere me lius quod ii l.</p>
  </div>
  <div class="service" style="left:827px">
    <div class="service-card"><div class="service-icon" role="img" aria-label="Icon of people in front of a globe"></div></div>
    <h3>Voicemail Transcription<br>for Service Providers /<br>Enterprises</h3>
    <p>Typi non habent claritatem insitam est usus legentis in iis qui facit eorum claritatem. Investigationes demonstrnt lectores legere me lius quod ii legunt.</p>
  </div>
</section>

<section class="testimonials">
  <h2>What People Say About KL9BQZ</h2>
  <div class="quote" style="left:37px">
    <div class="avatar" role="img" aria-label="Portrait photo of a smiling man" style="margin-left:84px"></div>
    <p>Vel illum dolore eu feugiat nulla facilisis at vero eros et accumsan et iusto dignissim qui blandit praesent lupt zril delenit augue duis dolore te feugait nulla facilisi.</p>
    <div class="name">Dorian Mallory</div>
    <div class="role">Accounting Officer</div>
  </div>
  <div class="quote" style="left:429px">
    <div class="avatar" role="img" aria-label="Portrait photo of a man in a suit" style="margin-left:86px"></div>
    <p>Typi non habent claritatem insitam est us legentis in iis qui facit eorum claritatem. Investigationes demonstraverunt lectores legere me lius quod ii legunt saepius.</p>
    <div class="name">Rowan Jesper</div>
    <div class="role">Accounting Officer</div>
  </div>
  <div class="quote" style="left:832px">
    <div class="avatar" role="img" aria-label="Portrait photo of a smiling woman" style="margin-left:92px"></div>
    <p>Claritas est etiam processus dynamicus sequitur mutationem consuetudium lectorum. Mirum est notare quam littera gothica, quam nunc pumus parum clam, anteposuerit litterarum formas.</p>
    <div class="name">Clara Menlow</div>
    <div class="role">President, CEO of Corvanta</div>
  </div>
</section>

<section class="cta">
  <p>Create your account today. No credit card required.</p>
  <div class="cta-btn">
    <svg width="40" height="40" viewBox="0 0 40 40" aria-hidden="true"><circle cx="20" cy="20" r="20" fill="#f09a2c"/><path d="M11 20h16M20 12l8 8-8 8" stroke="#fff" stroke-width="4" fill="none" stroke-linecap="round" stroke-linejoin="round"/></svg>
    GET STARTED
  </div>
</section>

<footer class="site-footer">
  <div class="brand"><span class="brand-dot"></span>kl9bqz</div>
  <div class="copyright">© 2014 KL9BQZ. All Rights Reserved.</div>
  <div class="footer-col" style="left:339px">
    <h4>CONNECT WITH US</h4>
    <div class="social"><span></span><span></span><span></span></div>
  </div>
  <div class="footer-col" style="left:632px">
    <h4>NAVIGATION</h4>
    <div class="links">
      <span>Home</span><span>Sitemap</span>
      <span>About</span><span>Webshop</span>
      <span>Products</span><span>Terms of Use</span>
      <span>Services</span><span>Privacy Policy</span>
      <span>Brands</span><span>Contact Us</span>
    </div>
  </div>
  <div class="footer-col" style="left:940px">
    <h4>CONTACT US</h4>
    <div class="contact">#38 street city, state, Country<br>email : info@tarvelo.com.au</div>
    <div class="phone">
      <svg width="30" height="30" viewBox="0 0 30 30" aria-hidden="true"><circle cx="15" cy="15" r="13" fill="none" stroke="#fff" stroke-width="2"/><path d="M10 8c-2 2 0 7 4 11s8 5 9 3l-3-3-2 1c-2-1-4-3-5-5l1-2z" fill="#fff"/></svg>
      012.555.0198
    </div>
  </div>
</footer>

</body>
</html>
```